Neudesign Homepage für Computerfirma
Zielgruppe
Wir sind ein seit 12 Jahren lokal ansässiger EDV Dienstleister mit Verkauf von PC, Notebooks etc. mit eigener Reparaturwerkstätte, Handel mit Computerzubehör. Zielgruppe: Klein- bis mittelständige Unternehmen / Organisationen, sowie Privatpersonen aller Altersgruppen.
Aufgabenstellung
Neudesign unserer Homepage: www.brivolt.at
responsives Design unter Beibehaltung unserer Logos bzw. Schriften und Farben( Logo kann gerne dezent verändert werden, aber die Charakteristik und Wiedererkennung muss bleiben ), gerne auch mit Webprogrammierung (CMS) welche aber separat ausgeschrieben/verhandelt wird. Seite soll komplett in HTML werden, technisch am Stand der Zeit mit allen Features die eine moderne HP haben soll.
Slogan "...damit Ihr Computer macht was er soll " wurde bisher schon oft verwendet und sollte wenn möglich eventuell untergebracht werden, gerne animiert.
Im Anhang einige bisher verwendete Grafiken zur Orientierung was bisher schon in Verwendung ist / war. (Bei Bedarf kann mehr geliefert werden)
Das Design sollte Kompetenz, Seriosität, renommiertes Unternehmen vermitteln. Kein Onlineshop momentan geplant. Schwerpunkt Reparatur/Wartung/Dienstleistung mit Ziel der Neukundengewinnung und Info für bestehende Kunden.
Grunddesign der Startseite, bei Bedarf je nach Designvorschlag auch Unterseite / Kontaktformular gerne im Direktauftrag, bei gefallen.

```html
<!DOCTYPE html>
<html lang="de">
<head>
<meta charset="utf-8">
<title>Brivolt – Easy IT-Solutions</title>
<link href="https://fonts.googleapis.com/css2?family=Open+Sans:wght@300;400;600;700;800&display=swap" rel="stylesheet">
<style>
:root{
  --green:#3aa12b;
  --ink:#231f20;
  --text:#222;
  --muted:#8a8a8a;
  --line:#d4d4d4;
  --panel:#ebebeb;
}
*{margin:0;padding:0;box-sizing:border-box}
html,body{width:789px;height:1200px;overflow:hidden;background:#fff}
body{font-family:'Open Sans',sans-serif;color:var(--text);position:relative}
.abs{position:absolute}
.nw{white-space:nowrap}

/* top bar */
.topbar{left:0;top:0;width:789px;height:20px;background:var(--green)}
.topbar .welcome{left:100px;top:5px;font-size:7px;color:#fff}
.social{right:128px;top:5px;display:flex;gap:9px}
.social span{width:10px;height:10px;border-radius:50%;background:#fff;display:block}

/* header */
.brand{left:95px;top:30px;font-size:31px;font-weight:800;color:var(--ink);letter-spacing:1px}
.header-line{left:0;top:64px;width:789px;height:2px;background:var(--green)}
.phone-icon{left:493px;top:26px}
.phone-label{left:520px;top:28px;font-size:7px;color:var(--green)}
.phone-number{left:520px;top:36px;font-size:19px;font-weight:600;color:var(--ink)}
.nav{left:0;top:87px;width:789px}
.nav a{position:absolute;font-size:8.5px;color:var(--ink);text-decoration:none}
.nav a.active{color:var(--green)}
.nav-rule{left:0;top:117px;width:789px;height:1px;background:#bdbdbd}

/* hero */
.hero-title{left:112px;top:160px;font-size:43px;font-weight:800;color:var(--ink);line-height:1}
.hero-sub{left:112px;top:207px;font-size:23px;font-weight:300;color:var(--ink);line-height:1}
.hero-copy{left:113px;top:246px;font-size:9px;line-height:12.6px;color:var(--muted)}
.btn{background:var(--green);color:#fff;text-decoration:none;display:flex;align-items:center;justify-content:center}
.hero-btn{left:113px;top:315px;width:120px;height:34px;font-size:8.5px}
.hero-visual{left:352px;top:138px;width:318px;height:240px;border-radius:6px;background:radial-gradient(ellipse at 50% 45%,#ffffff 0%,#e9e9e9 60%,#fff 100%)}
.hero-rule{left:0;top:397px;width:789px;height:2px;background:#cfcfcf}

/* welcome */
.welcome-band{left:0;top:399px;width:789px;height:280px;background:linear-gradient(#fff 0%,#fff 25%,#e4e4e4 100%)}
.portrait{left:80px;top:402px;width:168px;height:277px;background:linear-gradient(#e9e5dc,#d6d1c6);border-radius:40px 40px 0 0}
.welcome-title{left:258px;top:433px;font-size:18.5px;font-weight:700;color:var(--green)}
.welcome-sub{left:258px;top:456px;font-size:11px;font-weight:600;color:var(--ink)}
.welcome-copy{left:258px;top:486px;font-size:8.7px;line-height:12.6px;color:var(--ink);white-space:nowrap}
.welcome-copy p{margin-bottom:12.6px}
.green-rule{left:0;top:679px;width:789px;height:3px;background:var(--green)}

/* services */
.service{top:705px;width:220px;text-align:center}
.service .badge{width:95px;height:95px;border-radius:50%;border:1px solid #e2e2e2;margin:0 auto;display:flex;align-items:center;justify-content:center}
.service h3{margin-top:14px;font-size:15px;font-weight:600;color:var(--ink)}
.service h3 em{font-style:normal;font-weight:400;color:var(--green)}
.service .copy{margin-top:12px;font-size:8.7px;line-height:12.6px;color:var(--ink);white-space:nowrap}
.service .copy p{margin-bottom:12.6px}
.service-btn{top:960px;width:69px;height:23px;font-size:8.5px;font-weight:600}
.divider{top:705px;width:1px;height:278px;background:#e6e6e6}

/* footer links */
.sitemap{left:0;top:1016px;width:789px;height:130px;background:var(--panel)}
.col{top:1029px;width:138px;height:105px;border-left:1px solid #d6d6d6;padding-left:15px}
.col.last{border-right:1px solid #d6d6d6}
.col h4{font-size:11px;font-weight:600;color:var(--ink)}
.col h4 em{font-style:normal;color:var(--green)}
.col ul{list-style:none;margin-top:9px}
.col li{font-size:9px;line-height:12.6px;color:var(--muted);position:relative;padding-left:7px}
.col li::before{content:"";position:absolute;left:0;top:5px;width:3px;height:3px;background:var(--green)}

/* bottom bar */
.bottombar{left:0;top:1146px;width:789px;height:54px;background:var(--green)}
.foot-brand{left:110px;top:1161px;font-size:13px;font-weight:800;color:#fff;letter-spacing:.5px}
.copyright{left:198px;top:1167px;font-size:7.5px;color:#fff}
.legal{right:96px;top:1167px;font-size:7.5px;color:#fff}
</style>
</head>
<body>

<header>
  <div class="abs topbar">
    <div class="abs welcome">WILLKOMMEN AUF WWW.BRIVOLT.AT</div>
    <div class="abs social" aria-label="Soziale Netzwerke"><span></span><span></span><span></span><span></span><span></span></div>
  </div>

  <div class="abs brand">BRIVOLT</div>
  <div class="abs header-line" style="left:290px;width:499px"></div>

  <svg class="abs phone-icon" width="18" height="32" viewBox="0 0 18 32" aria-hidden="true">
    <rect x="1.5" y="1.5" width="15" height="29" rx="3" fill="none" stroke="var(--ink)" stroke-width="2.5"/>
    <line x1="4" y1="6" x2="14" y2="6" stroke="var(--ink)" stroke-width="1"/>
    <line x1="4" y1="24" x2="14" y2="24" stroke="var(--ink)" stroke-width="1"/>
    <circle cx="9" cy="27" r="1.4" fill="var(--ink)"/>
  </svg>
  <div class="abs phone-label">PROFESSIONELL BERATEN LASSEN:</div>
  <div class="abs phone-number">+43 5522 41870</div>

  <nav class="abs nav">
    <a class="active" style="left:314px">HOME</a>
    <a style="left:374px">NEWS</a>
    <a style="left:433px">SERIE</a>
    <a style="left:490px">LINE</a>
    <a style="left:543px">ANFAHRT</a>
    <a style="left:617px">KONTAKT</a>
  </nav>
  <div class="abs nav-rule"></div>
</header>

<section class="hero">
  <h1 class="abs hero-title">EASY</h1>
  <div class="abs hero-sub">IT-SOLUTIONS</div>
  <p class="abs hero-copy nw">Lorem ipsum dolor sit amet, consectetuer adipi-<br>scing elit, sed diam nonummy ibh euismod tinci-<br>dunt ut laoreet dolore magna aliquam erat<br>volutpat. Ut wisi en im ad minim veniam.</p>
  <a class="abs btn hero-btn">MEHR ERFAHREN</a>
  <div class="abs hero-visual" role="img" aria-label="Foto eines Desktop-Computers mit Monitor, Tastatur und Maus"></div>
  <div class="abs hero-rule"></div>
</section>

<section class="intro">
  <div class="abs welcome-band"></div>
  <div class="abs portrait" role="img" aria-label="Foto eines lächelnden Mitarbeiters mit Laptop unter dem Arm"></div>
  <h2 class="abs welcome-title nw">HERZLICH WILLKOMMEN BEI BRIVOLT!</h2>
  <div class="abs welcome-sub nw">IHR PARTNER IN SACHEN HARDWARE, SOFTWARE, PCREPARATUREN</div>
  <div class="abs welcome-copy">
    <p>Ein Ziel unserer Geschäftspolitik ist es, durch Zuverlässigkeit, Schnelligkeit und Kompetenz mit<br>unseren Kunden ein partnerschaftliches Verhältnis zu erreichen.</p>
    <p>Wenn Sie die Zusammenarbeit mit uns gewählt haben, werden Sie schnell feststellen, dass wir<br>als Ihr Geschäftspartner unser Hauptaugenmerk nicht allein auf den Vertrieb lenken, sondern als<br>Maxime allen Handelns die Zufriedenheit unserer Kunden in den Vordergrund stellen.</p>
    <p>Nicht nur durch jahrelange praktische Erfahrung wissen wir, dass eine faire, kompetente Bera-<br>tung und entsprechend praxisorientierte Problemlösung der Weg zu Ihrem Erfolg ist.</p>
    <p>Ein gewachsener Stamm überzeugter Kunden bestätigt die Anerkennung im Markt und ist ein<br>Beweis für die Richtigkeit unserer Geschäftspolitik.</p>
  </div>
  <div class="abs green-rule"></div>
</section>

<section class="services">
  <div class="abs service" style="left:25px">
    <div class="badge">
      <svg width="30" height="30" viewBox="0 0 30 30" aria-hidden="true">
        <circle cx="15" cy="11" r="7" fill="var(--green)"/>
        <path d="M7 11a8 8 0 0 1 16 0" fill="none" stroke="var(--green)" stroke-width="2"/>
        <path d="M2 30c0-7 6-11 13-11s13 4 13 11z" fill="var(--green)"/>
      </svg>
    </div>
    <h3>BRI<em>BERATUNG</em></h3>
    <div class="copy"><p>Die professionelle Betreuung und Beratung<br>des Kunden wird uns durch hochqualifi-<br>zierte Mitarbeiter gewährleistet, die durch<br>ständige Schulungen über alle Neuerungen<br>im Hard- und Softwarebereich umfassend<br>informiert sind.</p></div>
  </div>
  <a class="abs btn service-btn" style="left:100px">MEHR DAZU</a>
  <div class="abs divider" style="left:267px"></div>

  <div class="abs service" style="left:278px">
    <div class="badge">
      <svg width="54" height="46" viewBox="0 0 54 46" aria-hidden="true">
        <rect x="1.5" y="1.5" width="51" height="33" fill="none" stroke="var(--green)" stroke-width="3"/>
        <path d="M23 46l4-9 4 9z" fill="var(--green)"/>
        <path d="M18 28l10-10" stroke="var(--green)" stroke-width="4" stroke-linecap="round"/>
        <circle cx="31" cy="14" r="5" fill="var(--green)"/>
        <circle cx="33" cy="11" r="2.5" fill="#fff"/>
      </svg>
    </div>
    <h3>BRI<em>REPERATUR</em></h3>
    <div class="copy"><p>Privat oder gewerblich - hier sind Sie<br>richtig!</p><p>Wir überprüfen, reparieren und erweitern<br>Computer und Peripheriegeräte von sämtli-<br>chen Herstellern.</p></div>
  </div>
  <a class="abs btn service-btn" style="left:354px">MEHR DAZU</a>
  <div class="abs divider" style="left:521px"></div>

  <div class="abs service" style="left:533px">
    <div class="badge">
      <svg width="54" height="46" viewBox="0 0 54 46" aria-hidden="true">
        <rect x="1.5" y="1.5" width="51" height="33" fill="none" stroke="var(--green)" stroke-width="3"/>
        <path d="M23 46l4-9 4 9z" fill="var(--green)"/>
        <circle cx="27" cy="18" r="8" fill="none" stroke="var(--green)" stroke-width="3" stroke-dasharray="12 4"/>
      </svg>
    </div>
    <h3>BRI<em>RECYCLING</em></h3>
    <div class="copy"><p>Durch moderne Recyclingverfahren<br>können über 50 Prozent der Stoffe eines<br>PC´s wiederverwertet und wiedergewon-<br>nen und somit in den Rohstoffkreislauf<br>zurückgeführt werden.</p></div>
  </div>
  <a class="abs btn service-btn" style="left:608px">MEHR DAZU</a>
</section>

<footer>
  <div class="abs sitemap"></div>
  <div class="abs col" style="left:120px"><h4>BRI<em>VOLT</em></h4>
    <ul><li>Portrait</li><li>Portfolio</li><li>Handel</li><li>Dienstleistungen</li><li>Referenzen</li><li>Empfehlen Sie uns</li></ul></div>
  <div class="abs col" style="left:257px"><h4>BRI<em>NEWS</em></h4>
    <ul><li>Aktuell</li><li>Briflash</li><li>Projekte</li><li>Sponsoring</li></ul></div>
  <div class="abs col" style="left:395px"><h4>BRI<em>SERIE</em></h4>
    <ul><li>BriMobil</li><li>BriBeratung</li><li>BriPremium</li><li>BriReparatur</li><li>BriRecycling</li></ul></div>
  <div class="abs col last" style="left:532px"><h4>BRI<em>LINE</em></h4>
    <ul><li>PCNotdienst</li><li>Lageplan</li><li>Kontaktadressen</li><li>Kontakformualr</li><li>Öffnungszeiten</li></ul></div>

  <div class="abs bottombar"></div>
  <div class="abs foot-brand">BRIVOLT</div>
  <div class="abs copyright">COPYRIGHT 2014 BY BRIVOLT - COMPUTERSYSTEME-IT-SOLUTIONS</div>
  <div class="abs legal">KONTAKT | AGB | SITEMAP | IMPRESSUM</div>
</footer>

</body>
</html>
```